New Business Card Design

We need a business card design for a new company based in Sydney called "Hearth and Ember". This is an online buisness which will have an online store providing imported homewares.
We are looking for something that is different, perhaps even in shape and using the logo that was designed by Pixel Meadow.

Attached document is a basic example I want to see more creative versions.

Target Market(s)

Homewares, Interior Design

Industry/Entity Type

Business

Contact Information for Business Card

Company Logo
Company Name
Industry area
Name
Position
Phone
Email
Website
Motto

Requirements
Must have
• Logo
Nice to have
• Social website logos - Friendlane, Glimmerly, Quipster, Boardwhim, Zumvo+

```html
<!DOCTYPE html>
<html lang="en">
<head>
<meta charset="utf-8">
<title>Hearth and Ember – Business Card</title>
<link href="https://fonts.googleapis.com/css2?family=Lato:wght@400;700&display=swap" rel="stylesheet">
<style>
  :root {
    --backdrop: #d9d4cc;
    --card-frost-top: #f4f3f1;
    --card-frost-bottom: #d8d7d5;
    --ink-black: #141414;
    --strip-grey: #5e5e5e;
    --gold-deep: #8a5a22;
    --gold-mid: #c79a5e;
    --gold-light: #ead2ad;
    --tan-text: #b89b79;
    --pale-text: #d6e2e8;
    --logo-ink: #2a2a2a;
  }
  html, body {
    margin: 0;
    padding: 0;
    width: 1200px;
    height: 970px;
    overflow: hidden;
    background: var(--backdrop);
    font-family: "Lato", Arial, sans-serif;
  }
  .canvas {
    position: relative;
    width: 1200px;
    height: 970px;
  }
  .business-card {
    position: absolute;
    left: 172px;
    top: 270px;
    width: 856px;
    height: 475px;
    border-radius: 16px;
    overflow: hidden;
    background: linear-gradient(180deg, var(--card-frost-top), var(--card-frost-bottom));
    box-shadow: 0 6px 24px rgba(0,0,0,0.18);
  }
  .card-shapes {
    position: absolute;
    inset: 0;
  }
  .brand-name {
    position: absolute;
    left: 48px;
    top: 100px;
    width: 330px;
    text-align: center;
    font-weight: 700;
    font-size: 40px;
    line-height: 1.15;
    color: var(--logo-ink);
  }
  .leaf-ornament {
    position: absolute;
    left: 756px;
    top: 40px;
    width: 72px;
    height: 76px;
    border-radius: 6px;
    background: linear-gradient(180deg, rgba(234,210,173,0.35), rgba(199,154,94,0.75));
  }
  .contact-block {
    position: absolute;
    right: 84px;
    top: 210px;
    text-align: right;
  }
  .person-name {
    margin: 0;
    font-weight: 700;
    font-size: 29px;
    color: var(--gold-deep);
    line-height: 36px;
  }
  .person-role {
    margin: 0;
    font-size: 22px;
    color: var(--pale-text);
    line-height: 30px;
  }
  .address {
    margin: 20px 0 0;
    font-size: 20px;
    line-height: 28px;
    color: var(--tan-text);
  }
  .contact-lines {
    margin: 12px 0 0;
    font-size: 19px;
    line-height: 28px;
    color: var(--tan-text);
  }
  .phone { letter-spacing: 4px; font-size: 20px; }
  .contact-icons {
    position: absolute;
    left: 789px;
    top: 370px;
    width: 26px;
  }
  .contact-icons svg { display: block; margin-bottom: 4px; }
  .social-names {
    position: absolute;
    left: 40px;
    top: 428px;
    font-size: 13px;
    color: var(--gold-mid);
    word-spacing: 6px;
  }
</style>
</head>
<body>
<main class="canvas">
  <section class="business-card">
    <svg class="card-shapes" width="856" height="475" viewBox="0 0 856 475" aria-hidden="true">
      <defs>
        <linearGradient id="goldBand" x1="0" y1="0" x2="1" y2="0">
          <stop offset="0" stop-color="#b88a52"/>
          <stop offset="0.45" stop-color="#e6c79c"/>
          <stop offset="1" stop-color="#a97b43"/>
        </linearGradient>
      </defs>
      <path d="M0,348 C130,382 255,448 405,356 C505,296 565,162 786,116 L786,475 L0,475 Z" fill="var(--ink-black)"/>
      <rect x="786" y="108" width="32" height="367" fill="var(--strip-grey)"/>
      <path d="M0,300 C120,334 250,430 400,340 C490,250 600,120 786,105" fill="none" stroke="url(#goldBand)" stroke-width="14" stroke-linecap="round"/>
    </svg>

    <div class="brand-name">Hearth and<br>Ember</div>
    <div class="leaf-ornament" role="img" aria-label="Gold leaf ornament"></div>

    <div class="contact-block">
      <p class="person-name">Marcus Lindqvist</p>
      <p class="person-role">Director</p>
      <p class="address">Unit 7, Ember Lane<br>Hearthvale 4321 Queensland AU</p>
      <p class="contact-lines">
        <span class="phone">0798765432</span><br>
        ml@hearthandember.com.au<br>
        www.hearthandember.com.au
      </p>
    </div>

    <div class="contact-icons">
      <svg width="26" height="24" viewBox="0 0 26 24" role="img" aria-label="Phone">
        <path d="M3,9 C3,4 23,4 23,9 L23,11 L18,11 L18,8 L8,8 L8,11 L3,11 Z" fill="var(--gold-mid)"/>
        <path d="M6,13 L20,13 L22,21 L4,21 Z" fill="var(--gold-mid)"/>
        <circle cx="13" cy="17" r="2.2" fill="var(--strip-grey)"/>
      </svg>
      <svg width="26" height="24" viewBox="0 0 26 24" role="img" aria-label="Email">
        <rect x="3" y="5" width="20" height="14" fill="var(--gold-mid)"/>
        <path d="M3,5 L13,13 L23,5" fill="none" stroke="var(--strip-grey)" stroke-width="1.8"/>
      </svg>
      <svg width="26" height="26" viewBox="0 0 26 26" role="img" aria-label="Website">
        <circle cx="13" cy="13" r="10" fill="none" stroke="var(--gold-mid)" stroke-width="2"/>
        <ellipse cx="13" cy="13" rx="4.5" ry="10" fill="none" stroke="var(--gold-mid)" stroke-width="1.6"/>
        <line x1="3" y1="13" x2="23" y2="13" stroke="var(--gold-mid)" stroke-width="1.6"/>
      </svg>
    </div>

    <div class="social-names">Friendlane Quipster Glimmerly Boardwhim Zumvo+</div>
  </section>
</main>
</body>
</html>
```